Marketing Postcard Design for a Medical Supply Company

We are sending a marketing postcard to healthcare facilities within our state. We are in need of a design for a 6"x9" postcard, front and back with our logo, website www.carevale.shop, phone number 808-241-7739, and 12 products. The products are face shields, nitrile gloves, vinyl gloves, isolation gowns, gallon hand sanitizer, black KN95's, white KN95's, 4520 N95, 4530 N95, biohazard bags, Puratex wipes, and Kor spray. All of these items can be found on our website at carevale.shop. Please include a promo code, 10OFF for 10% Off. The design should be clean, professional, and appeal to a healthcare or medical audience.

```html
<!DOCTYPE html>
<html lang="en">
<head>
<meta charset="utf-8">
<title>Carevale Medical Supply – Postcard</title>
<link rel="stylesheet" href="https://fonts.googleapis.com/css2?family=Montserrat:wght@300;400;500;700;800&display=swap">
<style>
  :root{
    --green:#00914a;
    --green-dark:#0b5f32;
    --ink:#2d2d2d;
    --grey:#6b6b6b;
    --page-top:#e9ebee;
    --page-mid:#f6f7f8;
    --canvas:#ffffff;
  }
  *{box-sizing:border-box;margin:0;padding:0}
  html,body{width:1200px;height:1200px;overflow:hidden;background:var(--canvas)}
  body{font-family:'Montserrat',sans-serif;position:relative}
  .postcard{
    position:absolute;left:235px;top:47px;width:737px;height:1106px;overflow:hidden;
    background:linear-gradient(160deg,var(--page-top) 0%,var(--page-mid) 35%,#eceef0 60%,var(--page-mid) 100%);
  }
  .postcard > *{position:absolute}
  .headline{left:37px;top:44px;font-size:50px;font-weight:800;color:var(--green);letter-spacing:-0.5px;line-height:1}
  .subline{left:37px;top:94px;font-size:19.5px;font-weight:300;color:var(--grey);white-space:nowrap}
  .brand{left:560px;top:40px;width:160px;text-align:center}
  .brand-dot{width:44px;height:44px;border-radius:50%;background:var(--green);margin:0 auto 12px}
  .brand-name{font-size:23px;font-weight:800;color:var(--green);line-height:1}
  .brand-tag{font-size:8px;font-weight:800;color:var(--green);letter-spacing:2.2px;margin-top:3px}
  .intro{left:37px;top:172px;font-size:17.5px;font-weight:400;color:var(--ink);line-height:1.1;width:420px}
  .intro strong{color:var(--green);font-weight:700}
  .shop-btn{left:37px;top:238px;width:155px;height:44px;border-radius:22px;background:var(--green);
    color:#fff;font-weight:800;font-size:15px;display:flex;align-items:center;justify-content:center;
    box-shadow:0 3px 5px rgba(0,0,0,.25)}
  .collections{left:36px;top:350px;font-size:37px;font-weight:800;color:var(--green);letter-spacing:-0.3px}
  .promo-band{left:486px;top:302px;width:208px;height:76px}
  .promo-circle{left:386px;top:288px;width:112px;height:112px;border-radius:50%;background:var(--green);
    color:#fff;font-weight:700;text-align:center;display:flex;flex-direction:column;justify-content:center;line-height:1}
  .promo-circle .lbl{font-size:19px}
  .promo-circle .code{font-size:17px;margin-top:6px}
  .promo-off{left:505px;top:327px;font-size:31px;font-weight:700;color:#fff;white-space:nowrap}
  .product{width:176px;text-align:center}
  .product-ring{width:132px;height:132px;border-radius:50%;border:5px solid var(--green);background:#fff;
    margin:0 auto;overflow:hidden;display:flex;align-items:center;justify-content:center}
  .product-photo{width:92px;height:92px;border-radius:50%}
  .product-name{font-size:17.5px;font-weight:500;color:var(--ink);margin-top:24px;line-height:1}
  .footer{left:0;top:1033px;width:737px;height:47px;background:var(--green);color:#fff}
  .phone{position:absolute;left:37px;top:7px;display:flex;align-items:center;gap:10px;font-size:34px;font-weight:700}
  .web{position:absolute;right:49px;top:11px;font-size:20px;font-weight:300}
  .web b{font-weight:700}
</style>
</head>
<body>
<main class="postcard">
  <h1 class="headline">YOUR ONE</h1>
  <p class="subline">STOP SHOPFOR ALL OF YOUR SUPPLIES</p>

  <div class="brand">
    <div class="brand-dot"></div>
    <div class="brand-name">CAREVALE</div>
    <div class="brand-tag">MEDICAL SUPPLY</div>
  </div>

  <p class="intro"><strong>Health</strong> and safety supplies delivered to your business or the comfort of your own home</p>
  <div class="shop-btn">SHOP NOW</div>

  <h2 class="collections">COLLECTIONS</h2>

  <svg class="promo-band" viewBox="0 0 208 76">
    <polygon points="10,14 203,2 208,18 14,30" fill="var(--green)"/>
    <polygon points="10,20 190,18 208,24 196,74 10,72" fill="var(--green-dark)"/>
  </svg>
  <div class="promo-circle"><span class="lbl">Promo<br>Code:</span><span class="code">10OFF</span></div>
  <div class="promo-off">10% Off</div>

  <!-- row 1 -->
  <div class="product" style="left:20px;top:428px"><div class="product-ring"><div class="product-photo" role="img" aria-label="Teal face shield respirator" style="background:radial-gradient(circle,#2fb5b0,#1a8c89)"></div></div><p class="product-name">Face shields</p></div>
  <div class="product" style="left:188px;top:428px"><div class="product-ring"><div class="product-photo" role="img" aria-label="Box of blue nitrile gloves" style="background:radial-gradient(circle,#c9cfe0,#4a5a8a)"></div></div><p class="product-name">Nitrile gloves</p></div>
  <div class="product" style="left:363px;top:428px"><div class="product-ring"><div class="product-photo" role="img" aria-label="Stacked boxes of vinyl gloves" style="background:radial-gradient(circle,#f2f2f2,#d9a0a0)"></div></div><p class="product-name">Vinyl gloves</p></div>
  <div class="product" style="left:538px;top:428px"><div class="product-ring"><div class="product-photo" role="img" aria-label="Blue isolation gown" style="background:radial-gradient(circle,#5f8fd0,#2e5fa6)"></div></div><p class="product-name">Isolation gowns</p></div>

  <!-- row 2 -->
  <div class="product" style="left:20px;top:621px"><div class="product-ring"><div class="product-photo" role="img" aria-label="Gallon bucket of hand sanitizer" style="background:radial-gradient(circle,#e4e4e0,#9a9a96)"></div></div><p class="product-name" style="margin-top:22px">Gallon hand<br>sanitizer</p></div>
  <div class="product" style="left:188px;top:621px"><div class="product-ring"><div class="product-photo" role="img" aria-label="Black KN95 mask" style="background:radial-gradient(circle,#3a3a3a,#111)"></div></div><p class="product-name">Black KN95's</p></div>
  <div class="product" style="left:363px;top:621px"><div class="product-ring"><div class="product-photo" role="img" aria-label="White KN95 mask" style="background:radial-gradient(circle,#ffffff,#dcdcdc)"></div></div><p class="product-name">White KN95's</p></div>
  <div class="product" style="left:538px;top:621px"><div class="product-ring"><div class="product-photo" role="img" aria-label="White folded N95 respirator with red straps" style="background:radial-gradient(circle,#f0f0f0,#c9c9c9 70%,#c24040)"></div></div><p class="product-name">4520 N95</p></div>

  <!-- row 3 -->
  <div class="product" style="left:20px;top:827px"><div class="product-ring"><div class="product-photo" role="img" aria-label="Teal cup N95 respirator" style="background:radial-gradient(circle,#4cc3cc,#2a9aa6)"></div></div><p class="product-name">4530 N95</p></div>
  <div class="product" style="left:188px;top:827px"><div class="product-ring"><div class="product-photo" role="img" aria-label="Roll of red biohazard bags" style="background:radial-gradient(circle,#e03030,#b01818)"></div></div><p class="product-name">Biohazard bags</p></div>
  <div class="product" style="left:363px;top:827px"><div class="product-ring"><div class="product-photo" role="img" aria-label="Canister of Puratex disinfecting wipes" style="background:radial-gradient(circle,#ffffff,#c8ccd4)"></div></div><p class="product-name">Puratex wipes</p></div>
  <div class="product" style="left:538px;top:827px"><div class="product-ring"><div class="product-photo" role="img" aria-label="Jug of Kor disinfectant spray" style="background:radial-gradient(circle,#8cbf6a,#e8ece8)"></div></div><p class="product-name">Kor spray</p></div>

  <footer class="footer">
    <div class="phone">
      <svg width="31" height="31" viewBox="0 0 32 32" aria-hidden="true">
        <circle cx="16" cy="16" r="16" fill="#fff"/>
        <path d="M11.5 8.5c.6-.6 1.5-.5 2 .1l2 2.6c.4.6.4 1.3-.1 1.8l-1.3 1.3c.9 1.8 2.4 3.3 4.2 4.2l1.3-1.3c.5-.5 1.2-.5 1.8-.1l2.6 2c.6.5.7 1.4.1 2l-1.4 1.4c-1 1-2.6 1.2-3.9.5-3.6-1.9-6.6-4.9-8.5-8.5-.7-1.3-.5-2.9.5-3.9z" fill="var(--green)"/>
      </svg>
      808-241-7739
    </div>
    <div class="web">www.<b>carevale</b>.shop</div>
  </footer>
</main>
</body>
</html>
```